Webdesign für Reittherapeutin
Zielgruppe
Ich bin Reittherapeutin und biete auf unserem privaten Hof Reittherapie für Kinder, Jugendliche und Erwachsene an. Die Therapieeinheiten finden im Freien statt, also auf dem Sandplatz oder im Gelände. In der Reittherapie steht nicht das Reiten, sonden der Umgang und die Beziehung zum Pferd im Vordergrund.
Aufgabenstellung
Mir gefallen Designs in Naturtönen, welche auch gut zu meiner Tätigkeit passen. Ich habe bereits ein Logo, einen Namen (Wiesen erleben) und die Domaine (www.wiesen-erleben.ch) ebenso.

```html
<!DOCTYPE html>
<html lang="de">
<head>
<meta charset="utf-8">
<title>Wiesen erleben – Reittherapie</title>
<link rel="stylesheet" href="https://fonts.googleapis.com/css2?family=Fira+Sans:wght@300;400;500&family=Fira+Sans+Condensed:wght@400&family=Dancing+Script:wght@400&display=swap">
<style>
  :root {
    --page-bg: #9a9a9a;
    --sidebar-green: #b3bd6c;
    --nav-text: #5d5637;
    --logo-teal: #2a9fa3;
    --intro-bg: #ebe8e9;
    --body-text: #2f2f2f;
    --offer-bg: #6d6d6d;
    --offer-text: #f2f2f2;
    --accent-line: #c4cc7e;
    --hero-sky: #9fb6d4;
    --hero-field: #8f8a6d;
    --hero-ground: #c9bda8;
    --horse-dark: #2a2526;
  }
  * { box-sizing: border-box; margin: 0; padding: 0; }
  html, body { width: 1200px; height: 977px; overflow: hidden; }
  body {
    background: var(--page-bg);
    font-family: "Fira Sans", sans-serif;
    color: var(--body-text);
  }
  .site {
    position: relative;
    width: 1200px;
    height: 977px;
    display: grid;
    grid-template-columns: 180px 1fr;
  }
  .sidebar {
    background: var(--sidebar-green);
    display: flex;
    flex-direction: column;
  }
  .brand {
    background: #fff;
    height: 165px;
    display: flex;
    flex-direction: column;
    align-items: center;
    justify-content: center;
    gap: 14px;
  }
  .brand-dot {
    width: 56px; height: 56px;
    border-radius: 50%;
    background: var(--logo-teal);
  }
  .brand-name {
    font-family: "Fira Sans", sans-serif;
    font-weight: 400;
    font-size: 19px;
    color: var(--logo-teal);
  }
  .main-nav {
    list-style: none;
    margin-top: 44px;
    text-align: center;
  }
  .main-nav li {
    font-family: "Fira Sans Condensed", sans-serif;
    font-size: 17px;
    color: var(--nav-text);
    line-height: 48px;
  }
  .content { display: flex; flex-direction: column; }
  .hero {
    position: relative;
    height: 300px;
    background: linear-gradient(180deg, var(--hero-sky) 0%, #c4d0df 42%, var(--hero-field) 55%, var(--hero-ground) 100%);
  }
  .hero-photo-shade {
    position: absolute; inset: 0;
    background: linear-gradient(90deg, rgba(42,37,38,0) 0%, rgba(42,37,38,.55) 25%, rgba(42,37,38,.55) 55%, rgba(42,37,38,0) 70%);
  }
  .hero-title {
    position: absolute;
    right: 28px; bottom: 38px;
    text-align: right;
    color: #fff;
  }
  .hero-title h1 {
    font-weight: 400;
    font-size: 64px;
    letter-spacing: 2px;
    line-height: 1;
  }
  .hero-title p {
    font-size: 15px;
    letter-spacing: 1px;
    margin-top: 6px;
    color: #f0f0f0;
  }
  .intro {
    height: 345px;
    background: var(--intro-bg);
    display: flex;
    align-items: center;
    padding: 0 40px 0 62px;
    gap: 56px;
  }
  .intro-text { width: 410px; font-size: 12.5px; line-height: 1.55; }
  .intro-text p { margin-bottom: 7px; }
  .intro-sign {
    font-family: "Dancing Script", cursive;
    font-size: 21px;
    text-align: right;
    margin-top: 6px;
  }
  .intro-photo {
    width: 460px; height: 295px;
    background: linear-gradient(160deg, #b7c6da 0%, #cfc6b3 45%, #5a4d48 75%, var(--horse-dark) 100%);
  }
  .offers {
    flex: 1;
    background: var(--offer-bg);
    display: grid;
    grid-template-columns: repeat(3, 1fr);
    padding: 40px 30px 0;
  }
  .offer {
    display: flex;
    flex-direction: column;
    align-items: center;
    color: var(--offer-text);
    text-align: center;
  }
  .offer-icon { width: 60px; height: 60px; }
  .offer-icon-placeholder {
    width: 56px; height: 56px;
    border-radius: 8px;
    background: rgba(255,255,255,.22);
  }
  .offer h2 {
    font-weight: 400;
    font-size: 21px;
    letter-spacing: 1px;
    margin-top: 18px;
  }
  .offer h2::after {
    content: "";
    display: block;
    width: 26px; height: 2px;
    background: var(--accent-line);
    margin: 10px auto 0;
  }
  .offer p {
    width: 210px;
    font-size: 12.5px;
    line-height: 1.35;
    margin-top: 22px;
    min-height: 56px;
  }
  .more-link {
    margin-top: 30px;
    border: 1px solid var(--accent-line);
    color: var(--accent-line);
    font-size: 10.5px;
    letter-spacing: .5px;
    padding: 4px 12px;
  }
</style>
</head>
<body>
<div class="site">
  <aside class="sidebar">
    <div class="brand">
      <span class="brand-dot"></span>
      <span class="brand-name">Wiesen erleben</span>
    </div>
    <ul class="main-nav">
      <li>Reittherapie</li>
      <li>Angebot</li>
      <li>Über mich</li>
      <li>Pferde</li>
      <li>Kontakt</li>
    </ul>
  </aside>

  <main class="content">
    <section class="hero" role="img" aria-label="Foto: Reiterin liegt entspannt auf einem dunklen Pferd auf dem Sandplatz vor weiter Landschaft">
      <div class="hero-photo-shade"></div>
      <div class="hero-title">
        <h1>Reittherapie</h1>
        <p>Beziehung zwischen Mensch und Pferd</p>
      </div>
    </section>

    <section class="intro">
      <div class="intro-text">
        <p>In entspannter Atmosphäre dem Pferd begegnen.</p>
        <p>Freude, Motivation und Erfolgsmomente erfahren.</p>
        <p>Entspannung und Ruhe in der Natur finden.</p>
        <p>All das möchte ich meinen Klienten bieten und mit auf den Weg geben.</p>
        <p>Hab den Mut Dich zu melden!</p>
        <p class="intro-sign">Ich freue mich auf Dich!</p>
      </div>
      <div class="intro-photo" role="img" aria-label="Foto: Therapeutin mit Reithelm streichelt den Kopf eines schwarz-weissen Pferdes"></div>
    </section>

    <section class="offers">
      <article class="offer">
        <svg class="offer-icon" viewBox="0 0 60 60" fill="none" stroke="#f2f2f2" stroke-width="2">
          <circle cx="30" cy="20" r="10"/>
          <path d="M12 52c0-10 8-16 18-16s18 6 18 16z"/>
        </svg>
        <h2>Erstgespräch</h2>
        <p>Ein Erstgespräch vor dem Besuch der Reittherapie klärt viele offene Fragen.</p>
        <span class="more-link">&gt; MEHR DAZU</span>
      </article>
      <article class="offer">
        <div class="offer-icon-placeholder" role="img" aria-label="Symbol: Pferdekopf"></div>
        <h2>Schnupperstunde</h2>
        <p>Die Schnupperstunde ist dafür da, mich, die Pferde und die Stallumgebung kennen zu lernen.</p>
        <span class="more-link">&gt; MEHR DAZU</span>
      </article>
      <article class="offer">
        <div class="offer-icon-placeholder" role="img" aria-label="Symbol: Reiter auf Pferd"></div>
        <h2>Einzelstunde</h2>
        <p>In der Einzelstunde wird an den gemeinsamen formulierten Förderzielen und Wünschen Schritt für Schritt gearbeitet.</p>
        <span class="more-link">&gt; MEHR DAZU</span>
      </article>
    </section>
  </main>
</div>
</body>
</html>
```